Premium Skincare Packaging Design for Vale Hollow

Vale Hollow (https://valehollow-example.com) is a premium wellness brand from Canada specializing in beef tallow (for cooking) and now expanding into natural skincare. We are seeking packaging design concepts for two new 60 ml skincare products made with grass-fed beef tallow.
Our goal is to achieve a clean, minimalist yet luxurious look that reflects purity, quality and sophistication. The design should look premium enough for high-end skincare shelves while maintaining a natural, grounded feel.
You will be designing:
- Jar label (wrap-around design) for a 60 ml glass jar with black lid
- Round lid sticker (for the top of the black lid)
- Square outer box (for each jar)
- Both products are very similar, so the differentiation can be minimal.

Products to Design
1. All-Purpose Tallow Balm
Jar: Frosted glass, 60 ml with black lid
Purpose: Moisturizer for face, lips, hands, and body
Ingredients: Grass-fed beef tallow, beeswax, honey, vitamin E
Tone: Natural, pure, versatile, gentle
Tagline: “Crafted from nature’s simplest elements”
Preferred color palette:
Light / off-white background
Beige and honey accents
Black or dark brown typography
Mood: Minimalist apothecary meets warm, natural simplicity
2. Face Tallow Cream
Purpose: Face moisturizer with nourishing tallow and botanicals
Tone: Refined, elegant, modern, premium
Tagline: “The strength of tallow, refined for your face”
Preferred color palette:
Deep charcoal or black background
Gold or cream typography
Accent in subtle metallic tones (gold or bronze)
Mood: Modern luxury with understated confidence
Design Deliverables
For each product, submit:
1) Jar Label (Wrap-around)
- Include product name, logo, tagline, ingredients, and size (60 ml / 2 fl oz).
- Space for barcode and manufacturing details (leave placeholder).
2) Round Lid Sticker
- Centered logo and minimalist border or accent ring.
3) Outer Paper Box (Square)
- Matching color palette and typography.
- Clean layout featuring the Vale Hollow logo and tagline.
- Text to include: product name, tagline, ingredients and size.

Brand Guidelines
Logo: Use the existing Vale Hollow logo (we’ll upload it for reference).
Typography: Clean and elegant — sans-serif or classic serif fonts.
Tone: Pure, premium, and intentional — less is more.
Design cohesion: Both products must look like part of one collection.

```html
<!DOCTYPE html>
<html lang="en">
<head>
<meta charset="utf-8">
<title>Vale Hollow — Face Tallow Cream Packaging</title>
<link rel="stylesheet" href="https://fonts.googleapis.com/css2?family=Archivo:wght@500;700;800&family=Montserrat:wght@500&display=swap">
<style>
  :root {
    --page: #f6f6f6;
    --charcoal: #262424;
    --charcoal-soft: #343333;
    --cream-gold: #e6c597;
    --band-text: #2a2725;
  }
  * { margin: 0; padding: 0; box-sizing: border-box; }
  html, body { width: 1200px; height: 750px; overflow: hidden; background: var(--page); }
  body { position: relative; font-family: "Archivo", Arial, sans-serif; color: var(--cream-gold); }

  .panel { position: absolute; background: var(--charcoal); }

  /* Outer box */
  .box-side { left: 40px; top: 170px; width: 200px; height: 420px; background: var(--charcoal-soft); }
  .box-front { left: 240px; top: 170px; width: 420px; height: 420px; }

  .maker {
    position: absolute; left: 22px; bottom: 70px;
    font-size: 9px; font-weight: 500; line-height: 1.25; text-transform: none;
  }

  .brand {
    position: absolute; display: flex; align-items: center; gap: 10px;
    font-family: "Montserrat", Arial, sans-serif; font-weight: 500; letter-spacing: 0.08em;
    color: var(--cream-gold); white-space: nowrap;
  }
  .brand-mark { background: var(--cream-gold); flex: none; }

  .box-front .brand { right: 28px; top: 40px; font-size: 22px; }
  .box-front .brand-mark { width: 18px; height: 18px; }

  .title {
    position: absolute; font-weight: 800; text-transform: uppercase;
    line-height: 0.9; letter-spacing: 0.01em;
  }
  .box-front .title { left: 26px; top: 220px; font-size: 44px; }

  .band {
    position: absolute; background: var(--cream-gold); color: var(--band-text);
    font-weight: 700; text-transform: uppercase; white-space: nowrap;
  }
  .box-front .band { left: 26px; top: 345px; width: 370px; padding: 3px 8px; font-size: 9px; }

  .tagline { position: absolute; font-weight: 500; white-space: nowrap; }
  .box-front .tagline { left: 26px; top: 368px; font-size: 12px; border-bottom: 1.5px solid var(--cream-gold); padding-bottom: 3px; }

  .ingredients { position: absolute; font-weight: 500; line-height: 1.2; }
  .box-front .ingredients { left: 26px; top: 392px; font-size: 11px; }

  .size {
    position: absolute; font-size: 9px; font-weight: 500;
    writing-mode: vertical-rl; transform: rotate(180deg);
  }
  .box-front .size { right: 18px; top: 295px; }

  /* Lid sticker */
  .lid {
    position: absolute; left: 810px; top: 40px; width: 280px; height: 280px;
    border-radius: 50%; background: var(--charcoal);
    display: flex; align-items: center; justify-content: center;
  }
  .lid .brand { position: static; font-size: 22px; }
  .lid .brand-mark { width: 18px; height: 18px; }

  /* Jar label */
  .jar-label { left: 700px; top: 370px; width: 460px; height: 300px; }
  .jar-label .brand { right: 28px; top: 32px; font-size: 20px; }
  .jar-label .brand-mark { width: 16px; height: 16px; }
  .jar-label .title { left: 36px; top: 80px; font-size: 44px; }
  .jar-label .band { left: 36px; top: 205px; width: 390px; padding: 3px 8px; font-size: 9px; }
  .jar-label .tagline { left: 36px; top: 228px; font-size: 12px; border-bottom: 1.5px solid var(--cream-gold); padding-bottom: 3px; }
  .jar-label .ingredients { left: 36px; top: 252px; font-size: 11px; }
  .jar-label .size { right: 14px; top: 150px; }
</style>
</head>
<body>

  <section class="panel box-side" aria-label="Box side panel">
    <p class="maker">MANUFACTURED BY:<br>VALE HOLLOW, LLC<br>ADRESS orem ipsum 36 dolor sit<br>amet, CA</p>
  </section>

  <section class="panel box-front" aria-label="Box front panel">
    <div class="brand"><span class="brand-mark"></span>VALE HOLLOW</div>
    <h1 class="title">Face<br>Tallow<br>Cream</h1>
    <p class="band">Face moisturizer with nourishing tallow and botanicals</p>
    <p class="tagline">The strength of tallow, refined for your face</p>
    <p class="ingredients">Ingredients: Grass-fed beef tallow,<br>beeswax, honey, vitamin E</p>
    <p class="size">60ml 2oz</p>
  </section>

  <section class="lid" aria-label="Lid sticker">
    <div class="brand"><span class="brand-mark"></span>VALE HOLLOW</div>
  </section>

  <section class="panel jar-label" aria-label="Jar label">
    <div class="brand"><span class="brand-mark"></span>VALE HOLLOW</div>
    <h2 class="title">Face<br>Tallow<br>Cream</h2>
    <p class="band">Face moisturizer with nourishing tallow and botanicals</p>
    <p class="tagline">The strength of tallow, refined for your face</p>
    <p class="ingredients">Ingredients: Grass-fed beef tallow,<br>beeswax, honey, vitamin E</p>
    <p class="size">60ml 2oz</p>
  </section>

</body>
</html>
```